Business Card for Graphic Design Firm

This project is for a new graphic design firm based in Suite 210 called Velmoric. We outsource graphic design and marketing jobs. We want to communicate that this is a professional company but it as well creative and artistic. This card may be used as a horizontal double sided paper card or a vertical single sided translucent card so feel free to submit designs in whichever format or both.
Updates

Reason: Extending the deadline because I'm not exactly satisfied with the designs so far.

Please view the updated project brief

Target Market(s)

Adults aged 25-60

Industry/Entity Type

Graphic Design

Font styles to use
Serif
Sans Serif

Requirements
Nice to have
• Maybe a triangular pattern around the edges similar to our logo

```html
<!DOCTYPE html>
<html lang="en">
<head>
<meta charset="utf-8">
<title>Velmoric — Business Card, Front and Back</title>
<link rel="stylesheet" href="https://fonts.googleapis.com/css2?family=Mulish:wght@400;600;800&family=Questrial&display=swap">
<style>
  :root {
    --stage: #1f1f20;
    --card: #ffffff;
    --teal-deep: #0d7894;
    --teal: #0aa7b8;
    --sky: #74cbea;
    --amber: #fbb21c;
    --orange: #f47f22;
    --slate: #6d767b;
    --ink-name: #127d96;
    --ink-text: #5b6468;
    --label: #f2f2f2;
  }
  * { margin: 0; padding: 0; box-sizing: border-box; }
  html, body { width: 1200px; height: 849px; overflow: hidden; background: var(--stage); }
  .canvas { position: relative; width: 1200px; height: 849px; font-family: "Mulish", sans-serif; }
  .card-shapes { position: absolute; left: 0; top: 0; width: 1200px; height: 849px; }
  .card-surface { fill: var(--card); }
  .abs { position: absolute; white-space: nowrap; }
  .wordmark {
    font-family: "Mulish", sans-serif; font-weight: 600;
    color: var(--slate); letter-spacing: 2.5px; font-size: 14px; line-height: 1;
  }
  .holder-name { font-weight: 800; font-size: 15px; color: var(--ink-name); letter-spacing: 0.2px; line-height: 1; }
  .holder-role { font-weight: 600; font-size: 9.5px; color: var(--ink-text); letter-spacing: 0.3px; line-height: 1; }
  .contact-list { list-style: none; font-size: 10px; color: var(--ink-text); font-weight: 600; line-height: 1; }
  .contact-list li { position: absolute; white-space: nowrap; padding-left: 12px; }
  .contact-icon { position: absolute; left: 0; top: 1px; width: 9px; height: 8px; }
  .side-label { font-family: "Questrial", sans-serif; font-size: 31px; color: var(--label); line-height: 1; }
</style>
</head>
<body>
<main class="canvas">
  <svg class="card-shapes" viewBox="0 0 999 707">
    <defs>
      <linearGradient id="facetTones" x1="0" y1="0" x2="1" y2="1">
        <stop offset="0" stop-color="#0d7894"/>
        <stop offset="0.35" stop-color="#0aa7b8"/>
        <stop offset="0.55" stop-color="#74cbea"/>
        <stop offset="0.8" stop-color="#fbb21c"/>
        <stop offset="1" stop-color="#f47f22"/>
      </linearGradient>
      <linearGradient id="facetTonesBack" x1="1" y1="0" x2="0" y2="1">
        <stop offset="0" stop-color="#fbb21c"/>
        <stop offset="0.3" stop-color="#0aa7b8"/>
        <stop offset="0.6" stop-color="#74cbea"/>
        <stop offset="0.85" stop-color="#0d7894"/>
        <stop offset="1" stop-color="#f47f22"/>
      </linearGradient>
    </defs>

    <polygon class="card-surface" points="247,163 462,163 546,333 247,333"/>
    <polygon role="img" aria-label="Triangular facet pattern in teal, sky blue, amber, orange and slate"
             fill="url(#facetTones)" points="413,163 462,163 546,333 373,333"/>

    <polygon class="card-surface" points="553,372 753,372 753,543 455,543"/>
    <polygon role="img" aria-label="Triangular facet pattern in orange, amber, teal, sky blue and slate"
             fill="url(#facetTonesBack)" points="553,372 753,372 720,428 655,543 455,543"/>
  </svg>

  <section class="card card-front">
    <p class="abs wordmark" style="left:309px; top:257px;">VELMORIC</p>
    <h1 class="abs holder-name" style="left:308px; top:293px;">NAME SURNAME</h1>
    <p class="abs holder-role" style="left:309px; top:313px;">GENERAL MANAGER</p>
    <ul class="contact-list">
      <li style="left:309px; top:330px;">
        <svg class="contact-icon" viewBox="0 0 9 8"><polygon points="0,0 9,0 4.5,8" fill="var(--teal)"/></svg>
        48 Linden Lane
      </li>
      <li style="left:311px; top:343px;">Suite 210</li>
      <li style="left:309px; top:356px;">
        <svg class="contact-icon" viewBox="0 0 9 8"><polygon points="0,0 9,0 4.5,8" fill="var(--orange)"/></svg>
        (555) 014-2270
      </li>
      <li style="left:309px; top:371px;">
        <svg class="contact-icon" viewBox="0 0 9 8"><polygon points="0,0 9,0 4.5,8" fill="var(--amber)"/></svg>
        info@velmoric.com
      </li>
    </ul>
  </section>

  <section class="card card-back">
    <p class="abs wordmark" style="left:806px; top:627px;">VELMORIC</p>
  </section>

  <p class="abs side-label" style="left:695px; top:283px;">front</p>
  <p class="abs side-label" style="left:376px; top:533px;">back</p>
</main>
</body>
</html>
```